I need a very simple poster with the following quote:
"Cada escolha, uma renĂșncia, isso Ă© a vida"
Which means that to every choice there is a waiver, that's life.

It will be framed and used in my living room.

The poster has to be black and white. It is not mandatory to use commas and quotes.

The design has to be modern, like the references I posted on this board: http://pinboardly.example/marvetu/ideas/

```html
<!DOCTYPE html>
<html lang="pt">
<head>
<meta charset="utf-8">
<title>Cada escolha uma renúncia isso é a vida</title>
<link rel="stylesheet" href="https://fonts.googleapis.com/css2?family=Archivo:wdth,wght@62..125,100..900&display=swap">
<style>
  :root {
    --paper: #ffffff;
    --ink: #231f20;
  }
  html, body {
    margin: 0;
    padding: 0;
    width: 848px;
    height: 1200px;
    overflow: hidden;
    background: var(--paper);
  }
  .poster {
    display: block;
    width: 848px;
    height: 1200px;
    background: var(--paper);
  }
  .quote text {
    fill: var(--ink);
    font-family: "Archivo", "Helvetica Neue", Arial, sans-serif;
  }
  .word-cada {
    font-size: 218px;
    font-weight: 800;
    font-stretch: 75%;
  }
  .word-escolha {
    font-size: 104px;
    font-weight: 100;
    font-stretch: 100%;
  }
  .line-renuncia {
    font-size: 70px;
    font-stretch: 100%;
  }
  .line-isso {
    font-size: 100px;
    font-stretch: 100%;
  }
  .light { font-weight: 300; }
  .heavy { font-weight: 700; }
  .word-vida {
    font-size: 392px;
    font-weight: 900;
    font-stretch: 62%;
  }
</style>
</head>
<body>
  <svg class="poster" viewBox="0 0 848 1200" width="848" height="1200" role="img" aria-label="Cada escolha uma renúncia, isso é a vida">
    <g class="quote">
      <text class="word-cada" x="118" y="318" textLength="617" lengthAdjust="spacing">CADA</text>
      <text class="word-escolha" x="118" y="452" textLength="617" lengthAdjust="spacing">ESCOLHA</text>
      <text class="line-renuncia" x="118" y="562" textLength="617" lengthAdjust="spacing"><tspan class="light">UMA </tspan><tspan class="heavy">RENÚNCIA</tspan></text>
      <text class="line-isso" x="118" y="697" textLength="617" lengthAdjust="spacing"><tspan class="light">ISSO </tspan><tspan class="heavy">É</tspan><tspan class="light"> A</tspan></text>
      <text class="word-vida" x="110" y="1037" textLength="628" lengthAdjust="spacingAndGlyphs">VIDA</text>
    </g>
  </svg>
</body>
</html>
```